Print and E-book Personal Injury Front and Back Book Cover

I need a book cover for a personal injury law firm book titled "Beyond the Broken Road" with the subtitle "Making Sense of Accident Claims." The book cover should have an image. This isas a lead generation book designed to be give to potential clients to have them sign as new clients.

Target Market(s)

Potential New Clients Looking For a Personal Injury Attorney

Industry/Entity Type

Legal

Requirements
Must have
• Title and some type of image or images

```html
<!DOCTYPE html>
<html lang="en">
<head>
<meta charset="utf-8">
<title>Beyond the Broken Road – Book Cover</title>
<link rel="stylesheet" href="https://fonts.googleapis.com/css2?family=Antonio:wght@700&family=League+Gothic&display=swap">
<style>
  :root {
    --paper: #ffffff;
    --amber: #e8ad4a;
    --ink: #2f2a30;
    --cream: #eeeee4;
    --ink-soft: #3a343b;
  }
  * { margin: 0; padding: 0; box-sizing: border-box; }
  html, body {
    width: 1200px;
    height: 904px;
    overflow: hidden;
    background: var(--paper);
  }
  .canvas {
    position: relative;
    width: 1200px;
    height: 904px;
    background: var(--paper);
  }
  .back-cover {
    position: absolute;
    left: 123px;
    top: 114px;
    width: 477px;
    height: 675px;
    background: var(--amber);
  }
  .front-cover {
    position: absolute;
    left: 600px;
    top: 114px;
    width: 478px;
    height: 675px;
    background: var(--ink);
    overflow: hidden;
  }
  .hero-figure {
    position: absolute;
    left: 92px;
    top: 41px;
    width: 301px;
    height: 634px;
    background: linear-gradient(180deg, var(--ink-soft) 0%, var(--ink) 100%);
    border-radius: 120px 120px 0 0;
  }
  .title-block {
    position: absolute;
    left: 0;
    width: 100%;
    top: 290px;
    text-align: center;
  }
  .title-small {
    display: block;
    font-family: "League Gothic", "Arial Narrow", sans-serif;
    font-size: 36px;
    line-height: 36px;
    letter-spacing: 14px;
    padding-left: 14px;
    color: var(--cream);
  }
  .title-large {
    display: block;
    font-family: "Antonio", "Arial Narrow", sans-serif;
    font-weight: 700;
    font-size: 108px;
    line-height: 100px;
    letter-spacing: 2px;
    color: var(--amber);
    text-transform: uppercase;
  }
  .title-large + .title-large { margin-top: 4px; }
  .title-small { margin-bottom: 12px; }
  .subtitle {
    position: absolute;
    left: 0;
    width: 100%;
    top: 582px;
    text-align: center;
    font-family: "League Gothic", "Arial Narrow", sans-serif;
    font-size: 31px;
    line-height: 33px;
    letter-spacing: 5px;
    padding-left: 5px;
    color: var(--cream);
    text-transform: uppercase;
  }
</style>
</head>
<body>
  <main class="canvas">
    <section class="back-cover" aria-label="Back cover"></section>
    <section class="front-cover" aria-label="Front cover">
      <div class="hero-figure" role="img" aria-label="Line illustration of an injured man on a crutch raising a fist in strength"></div>
      <h1 class="title-block">
        <span class="title-small">BEYOND THE</span>
        <span class="title-large">Broken</span>
        <span class="title-large">Road</span>
      </h1>
      <p class="subtitle">Making Sense of<br>Accident Claims</p>
    </section>
  </main>
</body>
</html>
```